Packaging design for a reclosable bag for our product

We have a logo, and we need to put it on packaging for our product and while we want the look to be simple, we want it to follow good design principles and also contain spaces for other product descriptions.

There will be 5 sizes at launch so I'd like 5 variations, one for each size.

I've included a few mockups of the type of bag that I made but they are all just rough ideas that I had.

I want the brand to look scientific and methodical and even a bit quirky, as in "wow this is a serious product but also a bit unusual."

```html
<!DOCTYPE html>
<html lang="en">
<head>
<meta charset="utf-8">
<title>Orvel Bias Lighting – Pouch Range</title>
<link href="https://fonts.googleapis.com/css2?family=Open+Sans:wght@300;700&display=swap" rel="stylesheet">
<style>
  :root {
    --stage: #f4f4f4;
    --pouch: #000000;
    --band: #8a8a8a;
    --spec-text: #8c8c8c;
    --tag-ink: #111111;
    --size-xs: #d0232a;
    --size-s: #f7941d;
    --size-m: #f2e91a;
    --size-l: #127036;
    --size-xl: #164f9b;
  }
  * { margin: 0; padding: 0; box-sizing: border-box; }
  html, body {
    width: 1200px;
    height: 800px;
    overflow: hidden;
    background: var(--stage);
    font-family: "Open Sans", Arial, sans-serif;
  }
  .range {
    position: absolute;
    left: 35px;
    top: 251px;
    display: flex;
    gap: 20px;
  }
  .pouch {
    position: relative;
    width: 210px;
    height: 298px;
    background: var(--pouch);
    box-shadow: 4px 6px 10px rgba(0, 0, 0, 0.18);
  }
  .size-tag {
    position: absolute;
    top: 0;
    right: 0;
    width: 43px;
    height: 58px;
    clip-path: polygon(0 0, 100% 0, 100% 100%);
    background: var(--tag-color);
  }
  .size-tag span {
    position: absolute;
    top: 8px;
    right: 9px;
    font-weight: 700;
    font-size: 15px;
    line-height: 1;
    color: var(--tag-ink);
  }
  .size-xs { --tag-color: var(--size-xs); }
  .size-s  { --tag-color: var(--size-s); }
  .size-m  { --tag-color: var(--size-m); }
  .size-l  { --tag-color: var(--size-l); }
  .size-xl { --tag-color: var(--size-xl); }

  .brand-band {
    position: absolute;
    left: 0;
    top: 214px;
    width: 98px;
    height: 44px;
    background: var(--band);
    display: flex;
    align-items: center;
    justify-content: center;
  }
  .brand-name {
    font-weight: 700;
    font-size: 22px;
    letter-spacing: 0.5px;
    color: var(--pouch);
  }
  .spec-list {
    position: absolute;
    left: 105px;
    top: 212px;
    list-style: none;
    font-weight: 300;
    font-size: 8.4px;
    line-height: 9.4px;
    color: var(--spec-text);
    white-space: nowrap;
  }
</style>
</head>
<body>
  <main class="range">
    <article class="pouch size-xs">
      <div class="size-tag"><span>XS</span></div>
      <div class="brand-band"><span class="brand-name">Orvel</span></div>
      <ul class="spec-list">
        <li>1 Meter</li><li>Extra Large</li><li>Bias Lighting</li><li>Simulated D65 CRI 90+</li><li>6500K White</li>
      </ul>
    </article>
    <article class="pouch size-s">
      <div class="size-tag"><span>S</span></div>
      <div class="brand-band"><span class="brand-name">Orvel</span></div>
      <ul class="spec-list">
        <li>2 Meters</li><li>Extra Large</li><li>Bias Lighting</li><li>Simulated D65 CRI 90+</li><li>6500K White</li>
      </ul>
    </article>
    <article class="pouch size-m">
      <div class="size-tag"><span>M</span></div>
      <div class="brand-band"><span class="brand-name">Orvel</span></div>
      <ul class="spec-list">
        <li>3 Meters</li><li>Extra Large</li><li>Bias Lighting</li><li>Simulated D65 CRI 90+</li><li>6500K White</li>
      </ul>
    </article>
    <article class="pouch size-l">
      <div class="size-tag"><span>L</span></div>
      <div class="brand-band"><span class="brand-name">Orvel</span></div>
      <ul class="spec-list">
        <li>4 Meters</li><li>Extra Large</li><li>Bias Lighting</li><li>Simulated D65 CRI 90+</li><li>6500K White</li>
      </ul>
    </article>
    <article class="pouch size-xl">
      <div class="size-tag"><span>XL</span></div>
      <div class="brand-band"><span class="brand-name">Orvel</span></div>
      <ul class="spec-list">
        <li>5 Meters</li><li>Extra Large</li><li>Bias Lighting</li><li>Simulated D65 CRI 90+</li><li>6500K White</li>
      </ul>
    </article>
  </main>
</body>
</html>
```